Organization and people consulting firm needs a website design

I need a website that promotes and explains the consulting service we will provide. The organization is called Halcrest Consulting Group. Our services include organization design, employee experience, change management, and executive coaching. I would like to see a simple clean and professional design, that reflects a modern and forward looking professional services company

Target Market(s)

Mid market and large companies

Industry/Entity Type

Management Consulting

Coding

Coded - Design and coding required

Number of Pages Required

5+ page

Font styles to use
Sans Serif

Colors

Designer to choose colors to be used in the design.

Requirements
Must have
• The following pages: Home, The Way We Work, What We Do, Our Founder, Insights, Contact.
• Search button.
• Hyper links (will be provided with main body text)
• Scrolling website with summaries at top level and links to more detail at lower level (like this website: brightmaple.example)
• Company logo (uploaded)
• I have text for each of the pages that I can upload once the basic design is done
Should not have
• No clutter, keep the design clean

```html
<!DOCTYPE html>
<html lang="en">
<head>
<meta charset="utf-8">
<title>Halcrest Consulting Group</title>
<link href="https://fonts.googleapis.com/css2?family=Questrial&family=Lato:wght@400;700&display=swap" rel="stylesheet">
<style>
:root{
  --red:#e11f2d;
  --ink:#2f2f2f;
  --text:#444;
  --footer:#333335;
  --white:#fff;
  --rule:#d9d9d9;
}
*{box-sizing:border-box;margin:0;padding:0}
html,body{width:1200px;height:3435px;overflow:hidden;background:var(--white)}
body{position:relative;font-family:'Lato',sans-serif;color:var(--text)}
.backdrop{position:absolute;left:0;top:0}
.abs{position:absolute}
.brand{font-family:'Questrial',sans-serif;color:var(--white);letter-spacing:3px;display:flex;align-items:center;gap:12px}
.brand-dot{width:18px;height:18px;border-radius:50%;background:var(--white)}
.header-brand{left:103px;top:38px;font-size:30px}
.header-phone{left:676px;top:20px;color:var(--white);font-size:20px;display:flex;align-items:center;gap:10px}
.search{left:911px;top:16px;width:188px;height:38px;border:2px solid var(--white);border-radius:3px;color:var(--white);font-size:15px;padding:8px 10px;display:flex;justify-content:space-between;align-items:center}
.main-nav{left:498px;top:74px;display:flex;gap:25px;font-size:16px;color:var(--white)}
.hero-title{left:0;width:1200px;top:218px;text-align:center;color:var(--white);font-family:'Questrial',sans-serif;font-weight:700}
.hero-title .line1{font-size:56px;font-weight:700;letter-spacing:1px;line-height:1.1}
.hero-title .line2{font-size:52px;line-height:1.1}
.hero-tagline{left:0;width:1200px;top:358px;text-align:center;color:var(--white);font-size:21px;font-weight:700}
.slider-dots{left:1140px;top:230px;display:flex;flex-direction:column;gap:11px}
.slider-dots span{width:18px;height:18px;border-radius:50%;background:rgba(255,255,255,.6)}
.slider-dots span:first-child{background:var(--white)}
.section-title{font-family:'Questrial',sans-serif;font-size:46px;color:var(--ink);font-weight:700}
.section-title em{font-style:normal;color:var(--red)}
.centered{left:0;width:1200px;text-align:center}
.copy{font-size:14.5px;line-height:24px;color:var(--text)}
.copy-wide{left:100px;width:1000px;text-align:center}
.btn{display:flex;align-items:center;justify-content:center;background:var(--red);color:var(--white);font-size:15px;font-weight:700;border-radius:2px}
.btn-dark{background:var(--ink)}
.card{width:310px;height:328px;background:var(--white);box-shadow:0 0 8px rgba(0,0,0,.2);text-align:center;padding-top:28px}
.card-icon{width:60px;height:60px;margin:0 auto;border-radius:6px;background:#4a4a4a}
.card-icon.accent{background:var(--red)}
.card h3{font-family:'Questrial',sans-serif;font-size:19px;font-weight:700;color:var(--ink);margin-top:24px;letter-spacing:.5px}
.card h3.accent{color:var(--red)}
.card hr{width:84px;border:0;border-top:2px solid var(--ink);margin:18px auto 20px}
.card p{font-size:12.5px;line-height:20px;padding:0 22px}
.card .btn{width:100px;height:36px;margin:20px auto 0;font-size:14px}
.founder-photo{left:751px;top:2072px;width:332px;height:374px;background:linear-gradient(160deg,#c9b6a4,#8c6e58 55%,#5b4636);box-shadow:12px -10px 0 #f08a94}
.footer-brand{left:0;width:1200px;top:3120px;justify-content:center;font-size:36px}
.footer-contacts{left:0;width:1200px;top:3234px;display:flex;justify-content:center;gap:34px;color:var(--white);font-size:16px}
.footer-contacts span{display:flex;align-items:center;gap:10px}
.footer-nav{left:100px;width:1000px;top:3313px;display:flex;justify-content:space-between;color:var(--white);font-size:15px;font-weight:700;padding:0 58px}
.footer-rule{left:100px;width:1000px;top:3360px;border-top:1px solid #888}
.copyright{left:0;width:1200px;top:3390px;text-align:center;color:var(--white);font-size:13px;font-weight:700}
</style>
</head>
<body>

<svg class="backdrop" width="1200" height="3435" viewBox="0 0 1200 3435" aria-hidden="false">
  <defs>
    <linearGradient id="heroTone" x1="0" y1="0" x2="1" y2="1">
      <stop offset="0" stop-color="#8d9399"/>
      <stop offset=".5" stop-color="#5d636b"/>
      <stop offset="1" stop-color="#3d4148"/>
    </linearGradient>
    <linearGradient id="paleTone" x1="0" y1="0" x2="1" y2="1">
      <stop offset="0" stop-color="#f3f3f3"/>
      <stop offset="1" stop-color="#e4e4e4"/>
    </linearGradient>
  </defs>
  <polygon role="img" aria-label="Photo of a consulting team meeting around a table" fill="url(#heroTone)" points="0,0 1200,0 1200,530 847,660 0,538"/>
  <polygon fill="#000" opacity=".22" points="0,0 1200,0 1200,530 847,660 0,538"/>
  <polygon fill="var(--red)" points="0,546 847,668 1200,540 1200,550 847,684 0,554"/>

  <polygon role="img" aria-label="Faded photo of an open office" fill="url(#paleTone)" points="0,1271 348,1138 1200,1275 1200,1855 847,1983 0,1850"/>
  <polyline fill="none" stroke="var(--red)" stroke-width="8" points="0,1264 348,1134 1200,1268"/>
  <polyline fill="none" stroke="var(--red)" stroke-width="8" points="0,1856 847,1988 1200,1860"/>

  <polygon role="img" aria-label="Faded photo of colleagues at work" fill="url(#paleTone)" points="0,2634 348,2503 1200,2640 1200,2920 0,2920"/>
  <polyline fill="none" stroke="var(--red)" stroke-width="8" points="0,2627 348,2499 1200,2633"/>
  <polygon fill="var(--footer)" points="0,2926 847,3058 1200,2914 1200,3435 0,3435"/>
  <polygon fill="var(--red)" points="0,2914 847,3044 1200,2904 1200,2914 847,3060 0,2926"/>
</svg>

<header>
  <div class="abs brand header-brand"><span class="brand-dot"></span>HALCREST</div>
  <div class="abs header-phone">
    <svg width="30" height="30" viewBox="0 0 30 30"><circle cx="15" cy="15" r="13" fill="none" stroke="#fff" stroke-width="2"/><path d="M10 9c1-1 2-1 3 0l1 2c0 1-1 2-1 2 1 2 2 3 4 4 0 0 1-1 2-1l2 1c1 1 1 2 0 3-2 2-5 1-8-2s-4-6-3-9z" fill="#fff"/></svg>
    +1-555-014-2290
  </div>
  <div class="abs search">Search
    <svg width="14" height="14" viewBox="0 0 14 14"><circle cx="6" cy="6" r="4.5" fill="none" stroke="#fff" stroke-width="2"/><line x1="9" y1="9" x2="13" y2="13" stroke="#fff" stroke-width="2"/></svg>
  </div>
  <nav class="abs main-nav"><span>Home</span><span>The Way We Work</span><span>What We Do</span><span>Our Founder</span><span>Insights</span><span>Contact</span></nav>
</header>

<section>
  <div class="abs hero-title"><div class="line1">HALCREST CONSULTING</div><div class="line2">Group</div></div>
  <p class="abs hero-tagline">We are organisation &amp; people consulting firm.</p>
  <div class="abs slider-dots"><span></span><span></span><span></span><span></span><span></span></div>
</section>

<section>
  <h2 class="abs centered section-title" style="top:748px"><em>The Way</em> We Work</h2>
  <p class="abs copy copy-wide" style="top:846px">Nemo enim ipsam voluptatem quia voluptas sit aspernatur aut odit aut fugit, sed quia consequuntur magni dolores eos qui ratione voluptatem sequi nesciunt. Neque porro quisquam est, qui dolorem ipsum quia dolor sit amet, consectetur, adipisci velit, sed quia non numquam eius modi tempora incidunt ut labore et dolore magnam aliquam quaerat voluptatem.</p>
  <p class="abs copy copy-wide" style="top:936px">Neque porro quisquam est, qui dolorem ipsum quia dolor sit amet, consectetur, adipisci velit, sed quia non numquam eius modi tempora incidunt ut labore et dolore magnam aliquam quaerat voluptatem.</p>
  <a class="abs btn" style="left:531px;top:1030px;width:110px;height:44px">Read More</a>
</section>

<section>
  <h2 class="abs centered section-title" style="top:1264px"><em>What</em> We Do</h2>
  <p class="abs copy copy-wide" style="top:1368px">Nemo enim ipsam voluptatem quia voluptas sit aspernatur aut odit aut fugit, sed quia consequuntur magni dolores eos qui ratione voluptatem sequi nesciunt. Neque porro quisquam est, qui dolorem ipsum quia dolor sit amet.</p>
  <article class="abs card" style="left:101px;top:1466px">
    <div class="card-icon" role="img" aria-label="Presentation icon"></div>
    <h3>EMPLOYEE EXPERIENCE</h3><hr>
    <p>Nemo enim ipsam voluptatem quia voluptas sit aspernatur aut odit aut fugit, sed quia conse quuntur magni dolores.</p>
    <a class="btn btn-dark">Read More</a>
  </article>
  <article class="abs card" style="left:445px;top:1466px">
    <div class="card-icon accent" role="img" aria-label="Two people in conversation icon"></div>
    <h3 class="accent">CHANGE MANAGEMENT</h3><hr>
    <p>Nemo enim ipsam voluptatem quia voluptas sit aspernatur aut odit aut fugit, sed quia conse quuntur magni dolores.</p>
    <a class="btn">Read More</a>
  </article>
  <article class="abs card" style="left:789px;top:1466px">
    <div class="card-icon" role="img" aria-label="Coach with speech bubble icon"></div>
    <h3>EXECUTIVE COACHING</h3><hr>
    <p>Nemo enim ipsam voluptatem quia voluptas sit aspernatur aut odit aut fugit, sed quia conse quuntur magni dolores.</p>
    <a class="btn btn-dark">Read More</a>
  </article>
</section>

<section>
  <h2 class="abs section-title" style="left:101px;top:2052px"><em>Our</em> Founder</h2>
  <p class="abs copy" style="left:101px;top:2144px;width:590px">Nemo enim ipsam voluptatem quia voluptas sit aspernatur aut odit aut fugit, sed quia consequuntur magni dolores eos qui ratione voluptatem sequi nesciunt. Neque porro quisquam est, qui dolorem ipsum quia dolor sit amet, consectetur, adipisci velit, sed quia non numquam eius modi tempora incidunt ut labore et dolore magnam aliquam quaerat voluptatem.</p>
  <p class="abs copy" style="left:101px;top:2274px;width:590px">Neque porro quisquam est, qui dolorem ipsum quia dolor sit amet, consectetur, adipisci velit, sed quia non numquam eius modi tempora incidunt ut labore et dolore magnam aliquam quaerat voluptatem.</p>
  <a class="abs btn" style="left:101px;top:2386px;width:136px;height:42px">More About Him</a>
  <div class="abs founder-photo" role="img" aria-label="Portrait photo of the founder"></div>
</section>

<section>
  <h2 class="abs centered section-title" style="top:2644px"><em>Our</em> Insights</h2>
  <p class="abs centered" style="top:2726px;font-size:20px;color:var(--ink)">Get in touch with us and see how we can help</p>
  <p class="abs centered" style="top:2798px;font-size:15px;color:var(--ink)">48 Linden Hollow Road, Maple Cove, CT 06100, U.S.A.</p>
  <a class="abs btn" style="left:531px;top:2870px;width:111px;height:45px">Get in Touch</a>
</section>

<footer>
  <div class="abs brand footer-brand"><span class="brand-dot"></span>HALCREST</div>
  <div class="abs footer-contacts">
    <span><svg width="30" height="30" viewBox="0 0 30 30"><circle cx="15" cy="15" r="13" fill="none" stroke="#fff" stroke-width="2"/><path d="M10 9c1-1 2-1 3 0l1 2c0 1-1 2-1 2 1 2 2 3 4 4 0 0 1-1 2-1l2 1c1 1 1 2 0 3-2 2-5 1-8-2s-4-6-3-9z" fill="#fff"/></svg>+1-555-014-2290</span>
    <span><svg width="30" height="30" viewBox="0 0 30 30"><circle cx="15" cy="15" r="13" fill="none" stroke="#fff" stroke-width="2"/><rect x="8" y="10" width="14" height="10" fill="none" stroke="#fff" stroke-width="1.6"/><polyline points="8,10 15,16 22,10" fill="none" stroke="#fff" stroke-width="1.6"/></svg>m.halden@halcrestconsulting.example</span>
  </div>
  <nav class="abs footer-nav"><span>HOME</span><span>|</span><span>THE WAY WE WORK</span><span>|</span><span>WHAT WE DO</span><span>|</span><span>OUR FOUNDER</span><span>|</span><span>INSIGHTS</span><span>|</span><span>CONTACT</span></nav>
  <div class="abs footer-rule"></div>
  <p class="abs copyright">Copyrights @ 2018 Halcrest Consulting Group. All Rights Reserved.</p>
</footer>

</body>
</html>
```